Natural Skincare Product Labels Design

We are looking for a designer to create elegant but quirky, functional product labels for our natural skincare range.
The labels must reflect our brand’s values of simplicity, luxury, and the natural, handmade essence of our products.
https://www.pictogrove.com/marvellaskincare
1. Key Details
Packaging Dimensions
Container Types: Transparent jars.
Sizes for Body Products:
Diameter: 64mm–68mm.
Heights: 80mm, 88mm, and 97mm (lid height: 15mm).
Sizes for Face Creams:
Diameter: 60mm.
Height: 50mm (lid height: 15mm).
Label Fit: For body products, ideally one label size to fit all jar sizes.
For the smaller face cream jars, a separate, tailored label is required.
2. Label Placement
Options include a wrapped-around label or a combination of wrapped-around and top-of-jar elements.
Transparent jars mean the label must leave space for the product to be visible (e.g., partial wrap or cutout areas).
3. Content Requirements
Product Name: Prominently displayed.
Ingredient List: Dedicated space required.
Disclaimer/Usage Instructions: Include space for this information.
4. Design Goals
Look & Feel: Simple, upmarket, and natural, with a handmade essence.
Logo Usage: Our logo is finalized and available in gold, black, and white variants. Use Josefin Bold font for the logo if adjustments are required.
Color Palette: Neutral tones (e.g., whites, blacks, golds) are preferred, with flexibility for subtle pops of color tied to each product’s main ingredient.
5. Imagery
Open to including images and colours (e.g., botanical illustrations) that highlight the main ingredient (e.g., coffee beans, turmeric root, or honeycomb). Also open to labels having a prominent colour to tie it in to the main ingredient.
Alternatively, no images can also work for a clean design.
6. Current Design Context
Our temporary design features gold leaf on top and a simple handmade side label. We’re seeking to elevate this to a more polished, cohesive design.
7. Product Line
- Body Products (Larger Jars)
Tolo Body Butter
Key Ingredients: Guarana & Cupuaçu butter (inspired by Brazil).
Note: “Tolo” is slang for “bum.”
Manuka Honey Body Butter
Key Ingredients: Manuka honey (from New Zealand) & Cupuaçu butter.
Coffee Body Scrub
Key Ingredients: Coffee and Demerara sugar.
Whipped Body Soap - Turmeric
Key Ingredients: Turmeric and Bentonite clay.
Whipped Body Soap - Banana
- Face Products (Smaller Jars)
Face Cream
Key Ingredients: Carrot Oil and Raspberry Oil.
Features natural UV protection.
Good Night Cream
Key Ingredients: Enriched with Magnesium.
Promotes relaxation and restful sleep.
8. Submission Guidelines
Flexibility: Design should allow for consistent branding across all products while accommodating the varying jar sizes and ingredient focus.
Material Considerations: Labels should complement the transparent jars and allow the product inside to remain partially visible.
Print Elements: Incorporating gold accents is a plus but should not overpower the design.
We’re excited to see your vision for a label that celebrates the natural beauty and high quality of our skincare range. Please include mockups to showcase the design in use, particularly on transparent jars of varying sizes.
women 20-50 years of age

```html
<!DOCTYPE html>
<html lang="en">
<head>
<meta charset="utf-8">
<title>Marvella – Body Product Labels</title>
<link rel="stylesheet" href="https://fonts.googleapis.com/css2?family=Montserrat:wght@400;500&display=swap">
<style>
  :root {
    --ink: #1c1c1c;
    --paper: #ffffff;
    --stage: #f7f7f7;
    --edge: #dcdcdc;
    --tolo: #eab4c8;
    --coffee: #d9a184;
    --honey: #ecd27a;
  }
  * { margin: 0; padding: 0; box-sizing: border-box; }
  html, body {
    width: 1200px; height: 1200px; overflow: hidden;
    background: var(--paper);
    font-family: "Montserrat", sans-serif;
    color: var(--ink);
  }
  .canvas { position: relative; width: 1200px; height: 1200px; }
  .range-band {
    position: absolute; left: 6px; top: 22px; width: 1194px; height: 570px;
    background: var(--stage);
  }

  /* Shared label structure; each size sets its own measures */
  .label {
    position: absolute;
    width: var(--w); height: var(--h);
    background: var(--paper);
    overflow: hidden;
    text-align: center;
  }
  .label__accent {
    position: absolute;
    left: var(--accent-x); top: var(--accent-y);
    width: var(--accent-d); height: var(--accent-d);
    border-radius: 50%;
    background: var(--accent); opacity: .4;
  }
  .label__mark {
    position: absolute; left: 50%; top: var(--mark-y);
    width: var(--mark-d); height: var(--mark-d);
    margin-left: calc(var(--mark-d) / -2);
    border-radius: 50%;
    border: var(--mark-line) solid var(--ink);
  }
  .label__brand {
    position: absolute; left: 0; right: 0; top: var(--brand-y);
    font-size: var(--brand-size); font-weight: 500; line-height: 1;
    letter-spacing: .25em; padding-left: .25em;
    text-transform: uppercase;
  }
  .label__rule {
    position: absolute; left: var(--rule-x); width: var(--rule-w);
    height: var(--rule-line); background: var(--ink);
  }
  .label__rule--top { top: var(--rule1-y); }
  .label__rule--bottom { top: var(--rule2-y); }
  .label__title {
    position: absolute; left: 0; right: 0; top: var(--title-y);
    font-size: var(--title-size); font-weight: 400;
    line-height: var(--title-lead);
    letter-spacing: var(--title-track); padding-left: var(--title-track);
    text-transform: uppercase; white-space: nowrap;
  }
  .label__title span { display: block; }
  .label__ingredients {
    position: absolute; left: 0; right: 0; top: var(--ingr-y);
    font-size: var(--ingr-size); font-weight: 400;
    line-height: var(--ingr-lead);
    letter-spacing: var(--ingr-track); padding-left: var(--ingr-track);
    text-transform: uppercase; white-space: nowrap;
  }

  .label--small {
    --w: 337px; --h: 273px;
    --accent-x: 84px; --accent-y: 100px; --accent-d: 170px;
    --mark-y: 22px; --mark-d: 24px; --mark-line: 1.5px;
    --brand-y: 79px; --brand-size: 18px;
    --rule-x: 37px; --rule-w: 263px; --rule-line: 1px;
    --rule1-y: 149px; --rule2-y: 209px;
    --title-y: 154px; --title-size: 23px; --title-lead: 26px; --title-track: .15em;
    --ingr-y: 221px; --ingr-size: 10.5px; --ingr-lead: 14px; --ingr-track: .15em;
    border: 1px solid var(--edge);
  }
  .label--large {
    --w: 820px; --h: 421px;
    --accent-x: 290px; --accent-y: 170px; --accent-d: 240px;
    --mark-y: 36px; --mark-d: 44px; --mark-line: 2.5px;
    --brand-y: 123px; --brand-size: 28px;
    --rule-x: 181px; --rule-w: 428px; --rule-line: 2px;
    --rule1-y: 231px; --rule2-y: 326px;
    --title-y: 237px; --title-size: 34px; --title-lead: 42px; --title-track: .18em;
    --ingr-y: 344px; --ingr-size: 15px; --ingr-lead: 20px; --ingr-track: .22em;
    border: 1px solid var(--ink);
  }

  .label--tolo { --accent: var(--tolo); }
  .label--coffee { --accent: var(--coffee); }
  .label--honey { --accent: var(--honey); }

  .label--tolo.label--small { left: 49px; top: 208px; }
  .label--coffee.label--small { left: 452px; top: 205px; }
  .label--honey.label--small { left: 836px; top: 205px; }
  .label--coffee.label--large { left: 183px; top: 673px; }
</style>
</head>
<body>
<main class="canvas">
  <div class="range-band"></div>

  <section class="label label--small label--tolo">
    <div class="label__accent"></div>
    <div class="label__mark"></div>
    <p class="label__brand">Marvella</p>
    <div class="label__rule label__rule--top"></div>
    <h2 class="label__title"><span>Tolo</span><span>Body Butter</span></h2>
    <div class="label__rule label__rule--bottom"></div>
    <p class="label__ingredients">Guarana &amp; Cupuaçu Butter</p>
  </section>

  <section class="label label--small label--coffee">
    <div class="label__accent"></div>
    <div class="label__mark"></div>
    <p class="label__brand">Marvella</p>
    <div class="label__rule label__rule--top"></div>
    <h2 class="label__title"><span>Coffee</span><span>Body Scrub</span></h2>
    <div class="label__rule label__rule--bottom"></div>
    <p class="label__ingredients">Coffee and Demerara Sugar.</p>
  </section>

  <section class="label label--small label--honey">
    <div class="label__accent"></div>
    <div class="label__mark"></div>
    <p class="label__brand">Marvella</p>
    <div class="label__rule label__rule--top"></div>
    <h2 class="label__title"><span>Manuka Honey</span><span>Body Butter</span></h2>
    <div class="label__rule label__rule--bottom"></div>
    <p class="label__ingredients">Manuka Honey (from New Zealand)<br>&amp; Cupuaçu Butter.</p>
  </section>

  <section class="label label--large label--coffee">
    <div class="label__accent"></div>
    <div class="label__mark"></div>
    <p class="label__brand">Marvella</p>
    <div class="label__rule label__rule--top"></div>
    <h1 class="label__title"><span>Coffee</span><span>Body Scrub</span></h1>
    <div class="label__rule label__rule--bottom"></div>
    <p class="label__ingredients">Coffee and Demerara Sugar.</p>
  </section>
</main>
</body>
</html>
```